Insurance company needs a business card design

We need a business card design for a Massachusetts-based insurance company Veloria Insurance, LLC. We provide auto insurance to Hispanic (Spanish- or Portuguese-speaking) immigrants in the United States. We will give these business cards to auto dealers where such customers typically go to purchase vehicles. We will provide a solution to the dealers to provide easy insurance to the customers buying cars at their dealerships. Veloria is the Spanish word for protection.
Contact Information for Business Card
Name, Designation, Company Name, Address, Phone Number, Email, Website
Look and feel
Each slider illustrates characteristics of the customer's brand and the style your logo design should communicate.

```html
<!DOCTYPE html>
<html lang="en">
<head>
<meta charset="utf-8">
<title>Veloria Insurance – Business Card</title>
<link rel="stylesheet" href="https://fonts.googleapis.com/css2?family=Encode+Sans+Semi+Condensed:wght@300;400;600&display=swap">
<style>
  :root{
    --page:#ededee;
    --seal:#dcdddf;
    --card:#2c3031;
    --panel:#383d3e;
    --map:#596163;
    --map-faint:#323738;
    --white:#ffffff;
    --text:#e9ebec;
    --orange:#f0821e;
    --navy:#1f3f7a;
    --sheet:#eef0f2;
  }
  *{margin:0;padding:0;box-sizing:border-box}
  html,body{width:1200px;height:963px;overflow:hidden;background:var(--page)}
  body{position:relative;font-family:"Encode Sans Semi Condensed",sans-serif;font-weight:300;color:var(--text)}
  .seal-area{position:absolute;left:610px;top:233px;width:620px;height:620px;border-radius:50%;background:var(--seal);opacity:.7}
  .card{position:absolute;left:51px;width:617px;height:398px;border-radius:30px;background:var(--card);overflow:hidden;box-shadow:0 2px 6px rgba(0,0,0,.18)}
  .card--front{top:64px}
  .card--back{top:512px}

  /* front */
  .policy-sheet{position:absolute;left:218px;top:68px;width:349px;height:271px;border-radius:10px;background:var(--sheet);box-shadow:0 6px 14px rgba(0,0,0,.45);overflow:hidden}
  .brand{position:absolute;right:22px;top:34px;display:flex;align-items:center;gap:12px}
  .brand-mark{width:34px;height:34px;background:var(--navy)}
  .brand-name{font-size:34px;font-weight:600;color:var(--navy);letter-spacing:1px}
  .scene{position:absolute;left:0;right:0;bottom:0;height:122px;background:linear-gradient(180deg,#dfe7ee 0%,#c9d6e2 60%,#b8c7d6 100%)}
  .diagonal-panel{position:absolute;left:0;top:0;width:617px;height:398px;filter:drop-shadow(8px 0 10px rgba(0,0,0,.45))}
  .state-map{position:absolute;left:36px;top:33px;width:160px;height:88px;background:var(--map);border-radius:6px}

  .contact{position:absolute;left:36px;list-style:none;font-size:14.5px;line-height:20px}
  .contact li{display:flex;align-items:flex-start;gap:10px}
  .contact svg{flex:none;margin-top:3px}
  .contact--address{top:158px}
  .contact--online{top:222px}
  .contact--online li+li{margin-top:1px}
  .person{position:absolute;left:38px;top:320px}
  .person-name{font-size:34px;line-height:36px;color:var(--white)}
  .person-name span{color:var(--orange)}
  .person-role{font-size:14.5px;margin-top:1px}

  /* back */
  .intro{position:absolute;left:67px;top:40px;width:504px;font-size:14.5px;line-height:21px}
  .intro .line{display:block}
  .intro .line--full{text-align:justify;text-align-last:justify}
  .intro .accent{color:var(--orange)}
  .state-map--faint{position:absolute;left:56px;top:99px;width:560px;height:232px;background:var(--map-faint);border-radius:10px}
  .brand--back{position:absolute;left:67px;top:255px;font-size:30px;font-weight:400;color:var(--white)}
  .hotline{position:absolute;left:258px;top:205px;font-size:48px;line-height:56px;color:var(--white)}
  .rule{position:absolute;left:258px;right:0;top:269px;height:3px;background:var(--orange)}
  .hotline-note{position:absolute;left:258px;top:283px;width:318px;font-size:14.5px;line-height:21px}
  .hotline-note .line{display:block}
  .hotline-note .line--full{text-align:justify;text-align-last:justify}
</style>
</head>
<body>
  <div class="seal-area" role="img" aria-label="Faint state seal in the background"></div>

  <section class="card card--front">
    <div class="policy-sheet">
      <div class="brand">
        <span class="brand-mark"></span>
        <span class="brand-name">VELORIA</span>
      </div>
      <div class="scene" role="img" aria-label="Illustration of two cars after a minor accident with drivers on the phone, city skyline behind"></div>
    </div>

    <svg class="diagonal-panel" viewBox="0 0 617 398" aria-hidden="true">
      <polygon points="0,0 210,0 310,398 0,398" fill="var(--panel)"/>
    </svg>
    <div class="state-map" role="img" aria-label="Map outline of Massachusetts"></div>

    <ul class="contact contact--address">
      <li>
        <svg width="16" height="18" viewBox="0 0 16 18" aria-hidden="true"><path d="M8 1a6 6 0 0 1 6 6c0 4.5-6 10-6 10S2 11.5 2 7a6 6 0 0 1 6-6z" fill="none" stroke="currentColor" stroke-width="1.4"/><circle cx="8" cy="7" r="2.2" fill="none" stroke="currentColor" stroke-width="1.4"/></svg>
        <span>48 Harbor Row, Suite 305<br>Waltham, MA 02451</span>
      </li>
    </ul>
    <ul class="contact contact--online">
      <li>
        <svg width="15" height="15" viewBox="0 0 16 16" aria-hidden="true"><g fill="none" stroke="currentColor" stroke-width="1.2"><circle cx="8" cy="8" r="6.5"/><ellipse cx="8" cy="8" rx="3" ry="6.5"/><path d="M1.5 8h13M2.5 4.5h11M2.5 11.5h11"/></g></svg>
        <span>veloriainsurance.com</span>
      </li>
      <li>
        <svg width="15" height="15" viewBox="0 0 16 16" aria-hidden="true"><g fill="none" stroke="currentColor" stroke-width="1.2"><rect x="1.5" y="3.5" width="13" height="9" rx="1"/><path d="M1.5 4l6.5 5 6.5-5"/></g></svg>
        <span>info@veloriainsurance.com</span>
      </li>
      <li>
        <svg width="15" height="15" viewBox="0 0 16 16" aria-hidden="true"><path d="M3 1.5l3 3-1.6 1.8a9 9 0 0 0 5.3 5.3L11.5 10l3 3-2 2C6.5 15 1 9.5 1 3.5z" fill="none" stroke="currentColor" stroke-width="1.2" stroke-linejoin="round"/></svg>
        <span>(866) 555-0142 available 24 x 7</span>
      </li>
    </ul>

    <div class="person">
      <p class="person-name">DANA <span>MOREL</span></p>
      <p class="person-role">Insurance Agent</p>
    </div>
  </section>

  <section class="card card--back">
    <div class="state-map--faint" role="img" aria-label="Faint map outline of Massachusetts"></div>
    <p class="intro">
      <span class="line line--full"><span class="accent">Veloria</span> is an innovative company offering personal auto insurance for</span>
      <span class="line">Massachusetts drivers who struggle to find affordable coverage in the open market.</span>
    </p>
    <p class="brand--back">Veloria</p>
    <p class="hotline">(866) 555-0142</p>
    <div class="rule"></div>
    <p class="hotline-note">
      <span class="line line--full">Get in touch with one of our business development</span>
      <span class="line line--full">representatives in English, Spanish, or Portuguese</span>
    </p>
  </section>
</body>
</html>
```